Flyer to hand out to masters graduate students - giving glimpse of our training and placement progra

We are an IT consulting company, specialized in IT Training and placement programs for the IT graduates(masters students).I have attached the sample files, which we used for our previous fliers. Text (matter) remains same, but we need a new design. New colors. New logo is attached. Please come up with good images.

This is half folded flyer, which contains 4 faces.

Industry/Entity Type

It Company

```html
<!DOCTYPE html>
<html lang="en">
<head>
<meta charset="utf-8">
<title>Nexora Tech – Training &amp; Placement Program</title>
<link rel="stylesheet" href="https://fonts.googleapis.com/css2?family=PT+Sans:ital,wght@0,400;0,700;1,400&display=swap">
<style>
:root{
  --orange:#f0831e;
  --green:#7dbb2f;
  --green-dark:#5f9e1f;
  --blue:#1a6fc0;
  --blue-dark:#0f4f98;
  --text:#3a3a3a;
  --muted:#555;
  --paper:#ffffff;
  --line:#d9d9d9;
}
*{box-sizing:border-box;margin:0;padding:0}
html,body{width:1200px;height:907px;overflow:hidden;background:var(--paper)}
body{font-family:"PT Sans",Arial,sans-serif;color:var(--text)}
.flyer{position:relative;width:1200px;height:907px;overflow:hidden}
.panel{position:absolute;top:0;height:907px}
.panel-left{left:0;width:596px}
.panel-right{left:596px;width:604px;border-left:1px solid var(--line)}

.hero-photo{position:absolute;left:0;top:0;width:596px;height:235px;
  background:linear-gradient(135deg,#dfe4ea 0%,#c9ccd0 40%,#8a8f99 70%,#dfe2e6 100%)}
.hero-rule{position:absolute;left:0;top:235px;width:596px;height:5px;background:var(--green)}

.section-title{position:absolute;color:var(--orange);font-weight:700;font-size:18px}
.section-title::after{content:"";display:block;height:2px;background:var(--orange);margin-top:4px}
.about-title{left:38px;top:274px;width:152px}
.program-title{left:38px;top:535px;width:512px}
.features-title{left:622px;top:34px;width:146px}

.body-copy{position:absolute;font-size:12.4px;line-height:16.4px;text-align:justify;color:var(--text)}
.about-copy{left:38px;top:308px;width:528px}
.about-copy p+p{margin-top:16px}
.program-copy{left:38px;top:572px;width:528px}

.track-list{position:absolute;left:38px;top:640px;list-style:none;font-size:12.4px;line-height:23px}
.track-list li{display:flex;align-items:center;gap:6px}
.track-list svg{flex:none}

.closing-band{position:absolute;left:0;top:690px;width:596px;height:217px}
.closing-band svg{position:absolute;inset:0}
.closing-copy{position:absolute;left:60px;top:94px;width:478px;text-align:center;color:#fff;font-weight:700;font-size:13.2px;line-height:16.5px}

.feature-cols{position:absolute;left:622px;top:80px;width:560px;display:flex;gap:22px}
.feature-list{list-style:none;font-size:11.3px;line-height:13.6px;color:var(--muted)}
.feature-list li{position:relative;padding-left:12px;margin-bottom:8.5px}
.feature-list li::before{content:"";position:absolute;left:1px;top:5px;width:4px;height:4px;background:var(--muted)}
.feature-list.col-a{width:256px}
.feature-list.col-b{width:256px}

.referral-band{position:absolute;left:596px;top:332px;width:590px;height:118px;background:var(--green)}
.referral-photo{position:absolute;left:322px;top:0;width:268px;height:118px;
  background:linear-gradient(90deg,var(--green) 0%,#a6d46a 35%,#6f9a3e 70%,#9cc665 100%)}
.referral-copy{position:absolute;left:22px;top:11px;width:304px;text-align:center;color:#fff;font-weight:700;font-size:13.4px;line-height:17px}

.testimonials{position:absolute;left:622px;top:468px;width:538px;list-style:none}
.testimonial{font-size:12px;line-height:17.6px;text-align:justify;color:var(--text);margin-bottom:16px}
.testimonial .quote{color:var(--green);font-weight:700;font-size:30px;line-height:0;vertical-align:-10px;margin-right:6px;letter-spacing:-3px}
.testimonial .cite{white-space:nowrap}

.foot-rule{position:absolute;left:596px;top:873px;width:604px;height:34px;background:var(--green)}
</style>
</head>
<body>
<main class="flyer">

  <section class="panel panel-left">
    <div class="hero-photo" role="img" aria-label="Photo of young professionals smiling around a meeting table in an office"></div>
    <div class="hero-rule"></div>

    <h2 class="section-title about-title">About Us</h2>
    <div class="body-copy about-copy">
      <p>Nexora Tech, is one of the Leading IT consulting companies in US, with over 17 years proven industry track record, having top-tier enterprise companies as our clients &amp; training on Cutting Edge Technologies. We are Pioneers in Training &amp; Placements from Maple Ridge, New Jersey with Global presence in US and India. We distinguish ourselves from others through a quality of education, engineered by a dexterous mix of established teaching ideologies, modern methodologies and technically qualified instructors. Nexora Tech's methodologies make learning an enjoyable as well as a rewarding experience.</p>
      <p>Nexora Tech is currently hiring fresh graduates (OPT /CPT), willing to join us as Full-Time employees or Interns to cater the IT needs of our clients across USA. We provide free, top notch training, excellent accommodation and 100% guaranteed placements with H1B and green card sponsorship.</p>
    </div>

    <h2 class="section-title program-title">Nexora Tech's Student Training &amp; Placement Program Details</h2>
    <div class="body-copy program-copy">
      <p>Nexora Tech provides IT Training and computer education in almost all Programming, software, networking and Business applications to both IT and Non-IT graduates. We divide our courses into three categories depending on the background of the graduates.</p>
    </div>
    <ul class="track-list">
      <li><svg width="11" height="11" viewBox="0 0 11 11"><circle cx="5.5" cy="5.5" r="4" fill="none" stroke="#f0831e" stroke-width="2"/></svg>IT background Courses that suit programmers.</li>
      <li><svg width="11" height="11" viewBox="0 0 11 11"><circle cx="5.5" cy="5.5" r="4" fill="none" stroke="#f0831e" stroke-width="2"/></svg>IT Courses(Tools) that doesn't need any IT background.</li>
      <li><svg width="11" height="11" viewBox="0 0 11 11"><circle cx="5.5" cy="5.5" r="4" fill="none" stroke="#f0831e" stroke-width="2"/></svg>Courses that suit the business background.</li>
    </ul>

    <div class="closing-band">
      <svg width="596" height="217" viewBox="0 0 596 217" aria-hidden="true">
        <path d="M0 30 Q300 4 596 8 L596 217 L0 217 Z" fill="#7dbb2f"/>
        <path d="M0 42 Q300 14 596 20 L596 217 L0 217 Z" fill="#0f4f98"/>
        <path d="M0 54 Q300 32 596 36 L596 217 L0 217 Z" fill="#1a6fc0"/>
      </svg>
      <p class="closing-copy">We offer the courses, that are relevantly new, high in demand and has an excellent future in the IT sector, which enables us to proudly offer 100% guaranteed placements, attractive salaries and almost zero bench time between projects.</p>
    </div>
  </section>

  <section class="panel panel-right"></section>

  <h2 class="section-title features-title">Salient features</h2>
  <div class="feature-cols">
    <ul class="feature-list col-a">
      <li>Free training in courses that are in high demand and have excellent future in the IT sector.</li>
      <li>Professional, Dedicated and Certified Instructors with years of real time industry experience.</li>
      <li>Excellent one-on-one counseling to boost up your morale and confidence, preparing you to take that big leap into your future</li>
      <li>Extensive and well-planned course structure from a job point of view.</li>
      <li>Exposure to instructor's' real time work environments.</li>
      <li>Assistance in resume preparation, Interview preparation and job support after being placed.</li>
    </ul>
    <ul class="feature-list col-b">
      <li>100% guaranteed job placement through Nexora Tech 's excellent marketing team.</li>
      <li>Vast client base and preferred vendors for better billing rates in the industry.</li>
      <li>Rewarding Salary from the first day of the project</li>
      <li>Free Training / Financial Support / Free Accommodation / Relocation assistance / H1B Sponsorship / Green Card</li>
      <li>24/7 access to the labs.</li>
      <li>Zero Cost to you, until you receive your first paycheck</li>
    </ul>
  </div>

  <div class="referral-band">
    <div class="referral-photo" role="img" aria-label="Photo of a smiling young professional in a checked shirt on a green background"></div>
    <p class="referral-copy">We believe in word of mouth rather than any other means of marketing...so please reach out to us for the contacts of our real time employees who were in your shoes once and are successful IT professionals now.</p>
  </div>

  <ul class="testimonials">
    <li class="testimonial"><span class="quote">&#8220;&#8220;</span>Training, Accommodation, Placement can be provided by any consulting company, but, Nexora Tech stands out in equipping you for the first day of the job, and making sure that you sustain for the long term. In the past one year, I was on bench for just two days. <span class="cite">(Priya &nbsp;– CRM)</span></li>
    <li class="testimonial"><span class="quote">&#8220;&#8220;</span>Nexora Tech delivers everything they promise esp the lucrative salaries, which cannot be compared with any other companies.... I am earning more than my two year senior, from day one of my project. <span class="cite">(Ravi – Devops)</span></li>
    <li class="testimonial"><span class="quote">&#8220;&#8220;</span>Getting trained on totally new technologies in short period, and start working immediately at the client place is a big nightmare as a fresh graduate... but thanks to the Nexora Tech counseling team, who made the job so easy that... &nbsp;they really boosted up my morale to take the big leap and sustain further. <span class="cite">(Arjun – Mobile)</span></li>
    <li class="testimonial"><span class="quote">&#8220;&#8220;</span>Throughout my study life cycle my parents kept telling me, that almost every year is a crucial one... But Nexora Tech made me realize that these two months, with them are the most crucial period of my life, since I have to leap over this giant hurdle which connects the student life to the career life... Nexora Tech did an amazing job in walking me with confidence. That hurdle was a piece of cake. <span class="cite">(Meera – Big Data)</span></li>
    <li class="testimonial"><span class="quote">&#8220;&#8220;</span>Communication skills are the key to sustain in jobs in USA along with technical skills.... Nexora Tech stresses out this point from day one of their training, and guides us on how to handle at different real time job scenarios. This helped me to excel in the meetings and group discussions and sustain in my job. <span class="cite">( Kiran – Backend )</span></li>
  </ul>

  <div class="foot-rule"></div>
</main>
</body>
</html>
```